Cover and back of brochure

Our company sells all kind of filters. Now we are planning to create an image brochure for our company. This brochure should represent our high quality standard, our competence and the trust of the clients in our company.

In the attachment I added covers of other catalogs which we like. Furthermore I added nice pictures in the attachment which were downloaded from glimmerdock. In the first place we downloaded these pictures in a small size, so that several examples can be created. After we decide which picture looks best on the cover, we will buy it in a higher resolution.

More information you find in the added pdf document.

Industry/Entity Type

It Company

Colors

Designer to choose colors to be used in the design.

```html
<!DOCTYPE html>
<html lang="de">
<head>
<meta charset="utf-8">
<title>Brochure Cover and Back</title>
<link href="https://fonts.googleapis.com/css2?family=Josefin+Sans:wght@400;600;700&display=swap" rel="stylesheet">
<style>
  :root {
    --stage: #ececec;
    --ink: #2e4a0c;
    --leaf-light: #eaf6c8;
    --grass: #5fa322;
    --skin-soft: rgba(238, 214, 190, 0.7);
    --leaf-soft: rgba(120, 170, 70, 0.55);
  }
  * { margin: 0; padding: 0; box-sizing: border-box; }
  html, body { width: 1200px; height: 848px; overflow: hidden; background: var(--stage); }
  body { position: relative; font-family: "Josefin Sans", sans-serif; color: var(--ink); }

  .cover {
    position: absolute;
    top: 68px;
    width: 497px;
    height: 702px;
    overflow: hidden;
  }
  .cover--front { left: 96px; }
  .cover--back { left: 617px; }

  .cover__backdrop { position: absolute; inset: 0; }
  .cover--front .cover__backdrop {
    background:
      radial-gradient(ellipse 60% 40% at 50% 22%, #f3fbd9 0%, rgba(243,251,217,0) 70%),
      linear-gradient(180deg, #cfe98f 0%, #9fcf4e 45%, #7cb93a 75%, var(--grass) 100%);
  }
  .cover--back .cover__backdrop {
    background:
      radial-gradient(ellipse 55% 45% at 55% 45%, #fbffee 0%, rgba(251,255,238,0) 75%),
      linear-gradient(90deg, #8fc44a 0%, #cfe99a 30%, var(--leaf-light) 55%, #cfe99a 80%, #9acb55 100%);
  }

  .cover__photo {
    position: absolute;
    left: 82px; top: 222px;
    width: 364px; height: 376px;
    border-radius: 18px;
    background: linear-gradient(180deg, var(--skin-soft) 0%, var(--leaf-soft) 100%);
  }
  .cover__grass {
    position: absolute; left: 0; right: 0; bottom: 0; height: 110px;
    background: linear-gradient(180deg, rgba(95,163,34,0) 0%, #5a9e20 55%, #4a8a18 100%);
  }

  .cover__title {
    position: absolute; left: 0; right: 0; top: 108px;
    text-align: center; font-weight: 600; text-transform: uppercase; line-height: 1;
    white-space: nowrap;
  }
  .cover__title-line--top { display: block; font-size: 35px; letter-spacing: -0.3px; }
  .cover__title-line--bottom { display: block; font-size: 46px; margin-top: 10px; letter-spacing: 0.5px; }

  .contact {
    position: absolute; left: 0; right: 0; text-align: center; font-style: normal;
    text-transform: uppercase; font-weight: 600; font-size: 19px; line-height: 23px;
  }
  .contact--address { top: 164px; }
  .contact--lines { top: 293px; }
  .contact__rule {
    position: absolute; left: 50%; height: 2px; background: var(--ink);
    transform: translateX(-50%); width: 315px;
  }
  .contact__rule--first { top: 275px; }
  .contact__rule--second { top: 411px; width: 310px; }

  .tagline {
    position: absolute; left: 0; right: 0; top: 631px;
    text-align: center; text-transform: uppercase; font-weight: 600; font-size: 14px; letter-spacing: 0.3px;
  }
</style>
</head>
<body>
  <section class="cover cover--front">
    <div class="cover__backdrop" role="img" aria-label="Soft green bokeh background with fresh leaves in the top corners"></div>
    <div class="cover__photo" role="img" aria-label="Photo: two hands forming a roof over a small globe with trees growing on it"></div>
    <div class="cover__grass" role="img" aria-label="Fresh green grass along the bottom edge"></div>
    <h1 class="cover__title">
      <span class="cover__title-line--top">Filterkompetenz hat</span>
      <span class="cover__title-line--bottom">einen Namen</span>
    </h1>
  </section>

  <section class="cover cover--back">
    <div class="cover__backdrop" role="img" aria-label="Light green bokeh background framed by leaves in all four corners"></div>
    <address class="contact contact--address">
      Filter - Brandt e.K.<br>
      Inhaber Jonas Lehmkuhl<br>
      Lindauer Str. 14<br>
      12345 Berlin
    </address>
    <div class="contact__rule contact__rule--first"></div>
    <p class="contact contact--lines">
      Tel: 030 / 555 0142<br>
      Fax: 030 / 555 0143<br>
      E-Mail: info@filter-brandt.de<br>
      Web: www.filter-brandt.de
    </p>
    <div class="contact__rule contact__rule--second"></div>
    <p class="tagline">Kompetent | Hilfsbereit | Freundlich.</p>
  </section>
</body>
</html>
```